Corvane Lending Partners. Professional and Established Company

A full service finance company specializing in obtaining capital for small business. Business Lending advisor, helping small business owners access the capital they need to launch, grow, or sustain their business. Many of our programs offer flexible guidelines to overcome common obstacles such as credit score, credit history, and time in business, financials, and industry type. Our streamlined funding process makes getting a business loan, business line of credit, stated income commercial real estate loan, a smooth and stress free experience.SOME OF THE MOST COMMON NEEDS FOR BUSINESS CAPITAL:• Working Capital• Debt Consolidations (loans, merchant cash advances, etc.)• Payroll• Operating Expenses• Inventory• Equipment Financing• Commercial Real Estate (Purchase, Fix & Flip, Rehab, Renovations)• Business Acquisitions• Business ExpansionWe like the websites:www.brookfellcap.com they are in the same industry and provide the same servicesWe are wanting to be able to update when we do press releases and such using Word Press. Our look should be very professional and we will be adding Our Team Professional Bios and Headshots.

Industry/Entity Type

Finance

Number of Pages Required

5+ page

Font styles to use
Serif
Sans Serif

Requirements
Must have
• We want to copy brookfellcap.com
• We need:
• Home Page
• About Us
• Loan Programs
• Loan Criteria
• News
• Apply Now
• Contact
Nice to have
• See brookfellcap.com
Should not have
• Need professional design. Nothing bright or abstract

```html
<!DOCTYPE html>
<html lang="en">
<head>
<meta charset="utf-8">
<title>Corvane Lending Partners</title>
<link href="https://fonts.googleapis.com/css2?family=Open+Sans:wght@400;600;700&family=PT+Sans+Narrow:wght@400;700&family=Libre+Baskerville:wght@400&display=swap" rel="stylesheet">
<style>
:root{
  --brand-blue:#0b6cc2;
  --nav-blue:#2a7ab8;
  --title-blue:#1f86c6;
  --navy:#12284a;
  --orange:#f28a1a;
  --yellow:#f3d21c;
  --pale-yellow:#f2e27a;
  --card:#e8e8e8;
  --muted:#9a9a9a;
  --footer-bg:#f1f1f1;
  --green:#22b532;
  --white:#ffffff;
}
*{margin:0;padding:0;box-sizing:border-box}
html,body{width:1200px;height:3482px;overflow:hidden}
body{position:relative;font-family:"Open Sans",Arial,sans-serif;background:var(--white);color:#333}
.abs{position:absolute}

/* header */
.site-header{left:0;top:0;width:1200px;height:51px;background:var(--white)}
.logo-box{left:0;top:0;width:174px;height:88px;background:var(--white);z-index:3;padding:12px 14px}
.logo-name{font-family:"Libre Baskerville",Georgia,serif;font-size:15px;line-height:19px;color:var(--navy)}
.main-nav{left:265px;top:20px;font-size:14.5px;color:var(--nav-blue);letter-spacing:.2px;white-space:nowrap}
.main-nav span{margin:0 2px}
.util-links{left:928px;top:4px;font-size:8px;color:#555;display:flex;gap:26px}
.util-links i{display:inline-block;width:7px;height:6px;background:#777;margin-right:3px;vertical-align:middle}

/* hero */
.hero{left:0;top:51px;width:1200px;height:395px;background:linear-gradient(180deg,#1f4c7a 0%,#2a6fa4 35%,#1a3e6a 70%,#0e2446 100%)}
.hero-title{left:0;width:1200px;text-align:center;color:var(--white);font-weight:700;letter-spacing:1px}
.hero-title.one{top:152px;font-size:36px}
.hero-title.two{top:300px;font-size:36px}
.accent-band{left:0;top:446px;width:1200px;height:16px;background:var(--orange)}

/* intro */
.intro-bg{left:0;top:462px;width:1200px;height:982px;background:linear-gradient(180deg,#0d3a78 0%,#1d5fa8 40%,#133f77 75%,#0c2548 100%)}
.intro-tag{left:0;top:476px;width:1200px;text-align:center;color:var(--yellow);font-weight:700;font-size:24px}
.intro-sub{left:0;top:530px;width:1200px;text-align:center;color:var(--yellow);font-family:"PT Sans Narrow",sans-serif;font-weight:700;font-size:18px}
.intro-text{left:262px;top:576px;width:678px;text-align:center;color:var(--pale-yellow);font-family:"PT Sans Narrow",sans-serif;font-size:15px;line-height:20.5px}

/* cards */
.card{width:350px;background:var(--card);text-align:center}
.card h3{color:var(--title-blue);font-size:23px;font-weight:600}
.card p{color:#b0b0b0;font-size:10.5px;line-height:14px;width:240px;margin:0 auto}
.card .more{display:block;color:var(--title-blue);font-size:11.5px;font-weight:700;margin-top:18px}
.media{width:351px}

/* services */
.services{left:0;top:1444px;width:1200px;height:343px;background:var(--brand-blue)}
.services h2{left:0;top:1488px;width:1200px;text-align:center;color:#a9bfd2;font-size:21px;font-weight:700}
.service{width:240px;text-align:center;color:var(--white);font-weight:700;font-size:11.5px;line-height:14.5px}
.service svg{display:block;margin:0 auto 52px}

/* solutions */
.solutions-bg{left:0;top:1787px;width:1200px;height:662px;background:linear-gradient(180deg,#9fb2c2 0%,#6f879c 45%,#4a5d70 100%)}
.card.light{background:rgba(232,232,232,.93)}
.card.light h3{font-size:16px;font-weight:700;letter-spacing:.5px}

/* appointment */
.appointment-bg{left:0;top:2449px;width:1200px;height:529px;background:linear-gradient(90deg,#fbf9e2 0%,#eef0d4 18%,#a8b3bd 45%,#6b7f92 75%,#4c6278 100%)}
.appt-heading{left:246px;top:2490px;color:var(--navy);font-weight:700;font-size:15px}
.appt-lede{left:246px;top:2516px;color:#3c4a5a;font-size:10px;width:200px}
.emergency{left:248px;top:2630px;width:184px;height:148px;background:var(--white);padding:12px 8px}
.emergency h4{font-size:10.5px;font-weight:700;color:#222;margin-bottom:6px}
.phone-row{background:#e6e6e6;height:22px;font-size:10px;display:flex;align-items:center;gap:8px;padding-left:6px;margin-bottom:16px;color:#333}
.appt-form{left:460px;top:2483px;width:492px;height:453px;background:#f4f4f4;padding:0 14px}
.appt-form h3{font-size:17px;font-weight:400;color:#222;margin-top:6px}
.select-bar{left:14px;top:34px;width:216px;height:30px;background:var(--navy);color:var(--white);font-size:13px;font-weight:700;display:flex;align-items:center;padding-left:10px}
.select-bar svg{position:absolute;right:8px;top:8px}
.field-label{font-size:10.5px;color:#222}
.field{width:218px;height:20px;background:#e2e2e2;display:flex;align-items:center;justify-content:center;font-size:10px;color:#333}
.field.date{justify-content:space-between;padding:0 6px}
.message{left:14px;top:263px;width:466px;height:104px;background:#e2e2e2}
.book-btn{left:14px;top:397px;width:148px;height:22px;background:var(--green);color:var(--white);font-size:10.5px;font-weight:700;display:flex;align-items:center;justify-content:center;border-radius:3px}

/* instagram */
.insta{left:0;top:2978px;width:1200px;height:230px;background:var(--brand-blue)}
.insta-title{left:260px;top:3049px;color:var(--white);font-weight:700;font-size:14px}
.insta-handle{left:260px;top:3080px;color:#9ed0ff;font-size:9px}
.insta-img{top:2999px;width:161px;height:158px;border:2px solid var(--white)}

/* footer */
.site-footer{left:0;top:3208px;width:1200px;height:218px;background:var(--footer-bg)}
.foot-col{top:3240px}
.foot-col h5{font-size:11px;font-weight:700;color:#222;margin-bottom:16px}
.foot-col li{list-style:none;font-size:8.5px;color:#777;line-height:17px}
.email-line{width:150px;border-bottom:1px solid #999;font-size:10px;color:#888;padding-bottom:6px;margin-bottom:18px}
.subscribe{font-size:18px;font-weight:700;color:#333;margin-bottom:8px}
.socials{display:flex;gap:3px}
.socials span{width:14px;height:14px;background:var(--brand-blue);display:block}
.bottom-bar{left:0;top:3426px;width:1200px;height:56px;background:var(--brand-blue);color:#cfe3f7;font-size:8px}
.bottom-bar .copy{position:absolute;left:232px;top:24px}
.bottom-bar .legal{position:absolute;left:770px;top:24px}
</style>
</head>
<body>

<header class="abs site-header">
  <div class="abs logo-box"><div class="logo-name">Corvane Lending<br>Partners</div></div>
  <nav class="abs main-nav"><span>HOME PAGE</span> · <span>ABOUT US</span> · <span>LOAN PROGRAMS</span> · <span>LOAN CRITERIA</span> · <span>NEWS</span> · <span>APPLY NOW</span> · <span>CONTACT</span></nav>
  <div class="abs util-links"><span><i></i>E-Mail</span><span><i></i>LiveChat</span><span><i></i>Support</span></div>
</header>

<section>
  <div class="abs hero" role="img" aria-label="Night city skyline with glowing stock market chart lines"></div>
  <div class="abs hero-title one">CORVANE</div>
  <div class="abs hero-title two">LENDING PARTNERS</div>
  <div class="abs accent-band"></div>
</section>

<section>
  <div class="abs intro-bg" role="img" aria-label="City at night with light trails and financial data overlay"></div>
  <div class="abs intro-tag">CLP</div>
  <div class="abs intro-sub">Streamlined Funding Process Comes Easy</div>
  <p class="abs intro-text">A full service finance company specializing in obtaining capital for small business. Business Lending advisor, helping small business owners access the capital they need to launch, grow, or sustain their business. Many of our programs offer flexible guidelines to overcome common obstacles such as credit score, credit history, and time in business, financials, and industry type. Our streamlined funding process makes getting a business loan, business line of credit, stated income commercial real estate loan, a smooth and stress free experience. SOME OF THE MOST COMMON NEEDS FOR BUSINESS CAPITAL:</p>

  <div class="abs card" style="left:251px;top:680px;height:220px;padding-top:40px">
    <h3>Inventory</h3>
    <p style="margin-top:44px">The Halden Pumps TwinFlow two-stage rotary vane pumps with contactless, magnetically coupled drives</p>
    <span class="more">More Info</span>
  </div>
  <div class="abs media" style="left:601px;top:680px;height:220px;background:linear-gradient(135deg,#cfe3fb,#9cc4f2)" role="img" aria-label="Financial audit illustration with charts, calculator and magnifier"></div>

  <div class="abs media" style="left:251px;top:935px;height:221px;background:linear-gradient(135deg,#1e4f84,#0f2a4c)" role="img" aria-label="Businessman touching accounting, budget and report keywords"></div>
  <div class="abs card" style="left:602px;top:935px;height:221px;padding-top:42px">
    <h3>Working Capital</h3>
    <p style="margin-top:30px">The Halden Pumps TwinFlow two-stage rotary vane pumps with contactless, magnetically coupled drives</p>
    <span class="more">More Info</span>
  </div>

  <div class="abs card" style="left:251px;top:1188px;height:218px;padding-top:40px">
    <h3>Equipment Financing</h3>
    <p style="margin-top:26px">The Halden Pumps TwinFlow two-stage rotary vane pumps with contactless, magnetically coupled drives</p>
    <span class="more">More Info</span>
  </div>
  <div class="abs media" style="left:601px;top:1188px;height:218px;background:linear-gradient(135deg,#fbeef6,#f4c9df)" role="img" aria-label="Business statistics illustration with people on colourful chart blocks"></div>
</section>

<section>
  <div class="abs services"></div>
  <h2 class="abs">OUR SERVICES</h2>
  <div class="abs service" style="left:240px;top:1588px">
    <svg width="30" height="28" viewBox="0 0 30 28"><rect x="1" y="1" width="28" height="26" fill="#fff" stroke="#7ccf3a" stroke-width="3"/><path d="M8 14l5 5 9-10" fill="none" stroke="#1f7a2a" stroke-width="3"/></svg>
    The Halden Pumps TwinFlow two-stage rotary vane pumps with contactless, magnetically coupled drives are hermet
  </div>
  <div class="abs service" style="left:479px;top:1588px">
    <svg width="30" height="28" viewBox="0 0 30 28"><rect x="1" y="1" width="28" height="26" fill="#fff" stroke="#5c8be0" stroke-width="3"/><path d="M8 14l5 5 9-10" fill="none" stroke="#173c8a" stroke-width="3"/></svg>
    The Halden Pumps TwinFlow two-stage rotary vane pumps with contactless, magnetically coupled drives are hermet
  </div>
  <div class="abs service" style="left:720px;top:1588px">
    <svg width="30" height="28" viewBox="0 0 30 28"><rect x="1" y="1" width="28" height="26" fill="#fff" stroke="#f2d13a" stroke-width="3"/><path d="M8 14l5 5 9-10" fill="none" stroke="#2a2a2a" stroke-width="3"/></svg>
    The Halden Pumps TwinFlow two-stage rotary vane pumps with contactless, magnetically coupled drives are hermet
  </div>
</section>

<section>
  <div class="abs solutions-bg" role="img" aria-label="Businessman in front of glass office towers"></div>
  <div class="abs media" style="left:251px;top:1866px;height:246px;background:linear-gradient(135deg,#8ea3b6,#4f667d)" role="img" aria-label="Businessman drawing commercial real estate plans"></div>
  <div class="abs card light" style="left:251px;top:1866px;width:350px;height:246px;padding-top:76px;background:transparent">
    <h3 style="font-size:22px;font-weight:600">Commercial and Real Estate</h3>
    <p style="margin-top:40px;color:#e8eef3">The Halden Pumps TwinFlow two-stage rotary vane pumps with contactless, magnetically coupled drives</p>
  </div>
  <div class="abs card light" style="left:602px;top:1866px;height:246px;padding-top:86px">
    <h3>PAYROLL</h3>
    <p style="margin-top:46px">The Halden Pumps TwinFlow two-stage rotary vane pumps with contactless, magnetically coupled drives</p>
  </div>
  <div class="abs card light" style="left:251px;top:2161px;height:248px;padding-top:68px">
    <h3>OPERATING EXPENSES</h3>
    <p style="margin-top:46px">The Halden Pumps TwinFlow two-stage rotary vane pumps with contactless, magnetically coupled drives</p>
  </div>
  <div class="abs media" style="left:601px;top:2161px;height:248px;background:linear-gradient(135deg,#2e7c93,#163d57)" role="img" aria-label="Hand touching hexagon icons with taxes label"></div>
</section>

<section>
  <div class="abs appointment-bg" role="img" aria-label="Businessman in a bright office with city skyline"></div>
  <div class="abs appt-heading">FIX APPOINTMENT WITH US</div>
  <div class="abs appt-lede">Talk with a lending advisor today.</div>
  <div class="abs emergency">
    <h4>FOR EMERGENCY</h4>
    <div class="phone-row"><svg width="10" height="10" viewBox="0 0 10 10"><circle cx="5" cy="5" r="4.2" fill="none" stroke="#333" stroke-width="1.2"/><path d="M5 2.5v2.8l1.8 1" fill="none" stroke="#333" stroke-width="1.1"/></svg>+01-555-014-220</div>
    <h4>HOTLINE</h4>
    <div class="phone-row"><svg width="10" height="10" viewBox="0 0 10 10"><circle cx="5" cy="5" r="4.2" fill="none" stroke="#333" stroke-width="1.2"/><path d="M5 2.5v2.8l1.8 1" fill="none" stroke="#333" stroke-width="1.1"/></svg>+01-555-014-220</div>
  </div>

  <form class="abs appt-form">
    <h3>Fix An Appointment</h3>
    <div class="abs select-bar">Choose Services
      <svg width="14" height="14" viewBox="0 0 14 14"><rect x="1" y="1" width="12" height="12" fill="none" stroke="#fff"/><path d="M4 6l3 3 3-3" fill="none" stroke="#fff" stroke-width="1.3"/></svg>
    </div>
    <div class="abs" style="left:14px;top:86px"><div class="field-label">First Name</div><div class="field" style="margin-top:6px">&#9679;</div></div>
    <div class="abs" style="left:257px;top:86px"><div class="field-label">Last Name</div><div class="field" style="margin-top:6px">&#9679;</div></div>
    <div class="abs" style="left:14px;top:134px"><div class="field-label">Email Address</div><div class="field" style="margin-top:6px">@</div></div>
    <div class="abs" style="left:257px;top:134px"><div class="field-label">Phone Number</div><div class="field" style="margin-top:6px">&#9742;</div></div>
    <div class="abs" style="left:14px;top:184px"><div class="field-label">Select Date</div><div class="field date" style="margin-top:6px"><span>02-09-2018</span><span>&#9662;</span></div></div>
    <div class="abs" style="left:257px;top:184px"><div class="field-label">Social Security Number</div><div class="field" style="margin-top:6px">&#9679;</div></div>
    <div class="abs field-label" style="left:14px;top:246px">Compose Message</div>
    <div class="abs message"></div>
    <div class="abs book-btn">Book Appointment</div>
  </form>
</section>

<section>
  <div class="abs insta"></div>
  <div class="abs insta-title">Instagram</div>
  <div class="abs insta-handle">@corvane_lending</div>
  <div class="abs insta-img" style="left:422px;background:linear-gradient(135deg,#ffffff,#d9d9d9)" role="img" aria-label="Sketch of financial services concept diagram"></div>
  <div class="abs insta-img" style="left:608px;background:linear-gradient(135deg,#3b6f9c,#122c4a)" role="img" aria-label="Stock market chart on dark screen"></div>
  <div class="abs insta-img" style="left:794px;background:linear-gradient(135deg,#e7e9ec,#9fb1c4)" role="img" aria-label="Hands using a calculator over paperwork"></div>
</section>

<footer>
  <div class="abs site-footer"></div>
  <div class="abs foot-col" style="left:248px"><h5>London</h5><ul><li>Marketing Plan</li><li>Book Keeping</li><li>Credit Check</li><li>Loan Plans</li><li>Rate Review</li></ul></div>
  <div class="abs foot-col" style="left:422px"><h5>New York</h5><ul><li>Mortgage Calculator</li><li>Loan Matching</li><li>Personal Accounting</li><li>Tax Calculator</li></ul></div>
  <div class="abs foot-col" style="left:608px"><h5>Toronto</h5><ul><li>About Us</li><li>Press &amp; Media</li><li>News / Blogs</li><li>Careers</li><li>Awards &amp; Reviews</li><li>Testimonials</li></ul></div>
  <div class="abs foot-col" style="left:794px"><h5>Newsletter</h5>
    <div class="email-line">Your Email Address</div>
    <div class="subscribe">Subscribe</div>
    <div class="socials"><span></span><span></span><span></span><span></span><span></span></div>
  </div>
  <div class="abs bottom-bar">
    <span class="copy">Copyright © 2018 Corvane Lending Partners. All rights reserved.</span>
    <span class="legal">Terms of Service &nbsp;|&nbsp; Privacy Policy &nbsp;|&nbsp; Site Map</span>
  </div>
</footer>

</body>
</html>
```